Harlow Custom Boats Website update

I would like an updated website to my current site (Harlowboats.com).
I have an updated logo i would like to incorporate.
24 pages , would like to integrate videos of the boats (that i can upload later)

Target Market(s)

Professional and Commercial boat owners

Industry/Entity Type

Custom Boat Manufacturing

Coding

Coded - Design and coding required

Number of Pages Required

5+ page

Font styles to use
Serif

Requirements
Must have
• Easy to read, well laid-out, and video integration
Nice to have
• Fresh up to date look

```html
<!DOCTYPE html>
<html lang="en">
<head>
<meta charset="utf-8">
<title>Harlow Custom Boats</title>
<link href="https://fonts.googleapis.com/css2?family=Noto+Serif:wght@400;600;700&display=swap" rel="stylesheet">
<style>
:root{
  --navy:#1b3f94;
  --blue:#2350a8;
  --sky:#1e9be0;
  --ink:#1d2b3a;
  --teal-ink:#1f4e5f;
  --muted:#6a7480;
  --pale:#eef3fc;
  --grey-bar:#b4beb8;
  --white:#ffffff;
  --line:#dde2ea;
}
*{box-sizing:border-box;margin:0;padding:0}
html,body{width:1200px;height:1200px;overflow:hidden;background:var(--white)}
body{font-family:"Noto Serif",serif;color:var(--ink)}
.stage{position:absolute;left:427px;top:0;width:670px;height:1930px;transform:scale(0.6218);transform-origin:0 0;background:var(--white);overflow:hidden}
.abs{position:absolute}

/* header */
.site-header{position:absolute;left:0;top:0;width:670px;height:40px;background:linear-gradient(90deg,#2c52a6,#3458aa 60%,#2a4c9e)}
.brand-plate{position:absolute;left:0;top:0;width:145px;height:40px;background:var(--white);clip-path:polygon(0 0,100% 0,82% 100%,0 100%)}
.brand-name{position:absolute;left:14px;top:14px;font-size:8.5px;font-weight:700;color:var(--navy);white-space:nowrap}
.main-nav{position:absolute;left:219px;top:17px;display:flex;gap:10px;font-size:6px;font-weight:700;color:var(--white)}
.btn-appoint{position:absolute;left:366px;top:16px;width:82px;height:14px;background:var(--white);border-radius:2px;font-size:6.5px;color:var(--navy);text-align:center;line-height:14px}
.pill{position:absolute;top:14px;height:16px;border:1px solid var(--white);border-radius:9px;color:var(--white);font-size:5.5px;font-weight:700;line-height:14px;text-align:center}
.info-bar{position:absolute;left:0;top:40px;width:670px;height:15px;background:var(--grey-bar);font-size:5px;color:var(--navy)}
.info-bar span{position:absolute;top:4px}

/* hero */
.hero-photo{position:absolute;left:0;top:55px;width:670px;height:282px;background:linear-gradient(180deg,#3a62b8 0%,#6f88c4 30%,#a27155 55%,#d9dde2 78%,#c6cbd2 100%)}
.hero-panel{position:absolute;left:98px;top:73px;width:475px;height:192px;background:rgba(30,55,120,.72);border-bottom-right-radius:40px}
.hero-title{position:absolute;left:147px;top:103px;font-size:25px;font-weight:400;color:var(--white)}
.hero-title em{font-style:normal;color:#4cc1e6}
.hero-text{position:absolute;left:147px;top:141px;width:385px;font-size:10px;line-height:14.5px;color:#dfe6f2}
.hero-btn{position:absolute;left:147px;top:208px;width:95px;height:18px;background:#2a55b0;color:#d8e2f5;font-size:7px;letter-spacing:2px;text-align:center;line-height:18px}

/* about */
.about{position:absolute;left:0;top:337px;width:670px;height:218px;background:var(--pale)}
.section-title{font-size:17px;font-weight:400;color:var(--navy)}
.section-title em{font-style:normal;color:var(--sky)}
.about-text{position:absolute;left:57px;top:431px;width:260px;font-size:7.4px;line-height:10.4px;text-align:justify;color:var(--teal-ink)}
.about-photo{position:absolute;left:340px;top:379px;width:261px;height:139px;background:linear-gradient(135deg,#cfd6dc,#7f8e9c 45%,#2f4a7a 75%,#c9a77f)}

/* products */
.products-sub{position:absolute;left:0;top:616px;width:670px;text-align:center;font-size:7.5px;color:var(--ink)}
.card{position:absolute;width:175px;height:238px;background:var(--white);box-shadow:0 1px 4px rgba(0,0,0,.18)}
.card-img{position:absolute;left:5px;top:5px;width:165px;height:105px}
.card-title{position:absolute;left:0;top:118px;width:175px;text-align:center;font-size:8.5px;font-weight:700}
.card-text{position:absolute;left:6px;top:130px;width:163px;text-align:center;font-size:6.3px;line-height:9.3px;color:var(--muted)}
.card-btn{position:absolute;left:5px;width:165px;height:18px;background:var(--navy);color:var(--white);font-size:6.5px;text-align:center;line-height:18px}
.sea{background:linear-gradient(180deg,#6c9ed4 0%,#a9c6e2 45%,#3d8ab0 70%,#2b7aa2 100%)}
.dusk{background:linear-gradient(180deg,#1a1c22 0%,#6b6f86 40%,#c98a6a 52%,#2a3a48 70%,#151a20 100%)}
.deep{background:linear-gradient(180deg,#2d6fc0 0%,#3f87cc 55%,#1c5a9e 100%)}
.bright{background:linear-gradient(180deg,#5b9ee0 0%,#bcd3ea 50%,#d9d4c2 80%,#b8a98a 100%)}

/* gallery */
.gallery{position:absolute;left:0;top:1173px;width:670px;height:227px;background:linear-gradient(120deg,#eaf2fb,#f4f8fc)}
.field-label{position:absolute;left:57px;top:1244px;font-size:7.5px;color:var(--navy)}
.select{position:absolute;left:57px;top:1258px;width:260px;height:20px;background:var(--white);border:1px solid var(--line);font-size:6px;line-height:18px;padding-left:8px}
.select::after{content:"⌄";position:absolute;right:5px;top:-3px;font-size:8px}
.gallery-text{position:absolute;left:57px;top:1287px;width:260px;font-size:7.4px;line-height:10.4px;text-align:justify;color:var(--teal-ink)}
.video{position:absolute;left:340px;top:1215px;width:261px;height:139px;background:linear-gradient(180deg,#2f6cbf 0%,#3e88cf 50%,#1d5da3 100%)}
.video-bar{position:absolute;left:8px;bottom:8px;width:245px;height:14px;color:var(--white);font-size:6.5px}

/* contact */
.contact-info{position:absolute;left:80px;top:1488px;width:200px;text-align:center;font-size:7.4px;line-height:10.4px;color:#3c4654}
.contact-info .mini-brand{font-size:9px;font-weight:700;color:var(--navy);margin-bottom:18px}
.divider{position:absolute;left:336px;top:1450px;width:1px;height:230px;background:#eef1f5}
.form-label{position:absolute;left:351px;font-size:7.5px;color:var(--ink)}
.input{position:absolute;left:413px;width:201px;height:20px;border:1px solid var(--line);background:var(--white);font-size:6px;color:#8a93a0;padding:6px 6px}
.submit{position:absolute;left:413px;top:1666px;width:96px;height:18px;background:var(--navy);color:var(--white);font-size:7px;letter-spacing:2px;text-align:center;line-height:18px}

/* footer */
.footer-wave{position:absolute;left:0;top:1675px;width:670px;height:255px}
.footer-brand{position:absolute;left:68px;top:1808px;width:120px;font-size:15px;line-height:19px;font-weight:700;color:var(--white)}
.foot-col{position:absolute;top:1792px;font-size:6.2px;line-height:9.2px;color:#d6e2f6;white-space:nowrap}
.foot-col h4{font-size:9.5px;font-weight:400;color:var(--white);margin-bottom:1px}
.social{display:flex;gap:17px;margin-top:6px}
.social i{display:block;width:12px;height:12px;border-radius:50%;background:var(--white)}
</style>
</head>
<body>
<div class="stage">

  <header class="site-header">
    <div class="brand-plate"></div>
    <div class="brand-name">Harlow Custom Boats</div>
    <nav class="main-nav"><span>About Us</span><span>Products</span><span>Gallery</span><span>Contact Us</span></nav>
    <div class="btn-appoint">Request Appointment</div>
    <div class="pill" style="left:560px;width:34px">→ Join</div>
    <div class="pill" style="left:604px;width:44px">👤 Sign-in</div>
  </header>
  <div class="info-bar">
    <span style="left:487px">✆ (555) 201-4470</span>
    <span style="left:556px">✉ Office@harlowboats.com</span>
  </div>

  <section>
    <div class="hero-photo" role="img" aria-label="White custom sport fishing boat on the water beside rocky hills"></div>
    <div class="hero-panel"></div>
    <h1 class="hero-title">Welcome to <em>Harlow Boats</em></h1>
    <p class="hero-text">We build custom boats to meet our customers' specification. Our boats range in size from 26' to 71'. We specialize in Dive Boats, Yacht Sport Fisherman, Patrol Boats, and Research Vessels. Our projects are original and diverse. Quality and customer satisfaction are always our top priorities.</p>
    <div class="hero-btn">Contact Us</div>
  </section>

  <section class="about"></section>
  <h2 class="section-title abs" style="left:57px;top:404px">About <em>Us</em></h2>
  <p class="about-text">We are a professional and experienced team in boat building, which is very important to ensure comfort and optimal performance, with quality materials and the use of modern technology as a system that controls and controls boat performance.</p>
  <div class="about-photo" role="img" aria-label="Team meeting around an office table"></div>

  <h2 class="section-title abs" style="left:0;top:588px;width:670px;text-align:center">Our <em>Products</em></h2>
  <p class="products-sub">Explore range of our boat products</p>

  <article class="card" style="left:53px;top:641px">
    <div class="card-img dusk" role="img" aria-label="Boats moored in a bay at sunset"></div>
    <h3 class="card-title">71' Custom Dive</h3>
    <p class="card-text">The "New" Harlow 71' x 18' model is now available and the custom possibilities are endless. With over 252 square feet in the salon area and over 240 square feet below, there will be plenty of room for all the amenities you desire.</p>
    <div class="card-btn" style="top:182px">Read more</div>
  </article>
  <article class="card" style="left:249px;top:641px">
    <div class="card-img sea" role="img" aria-label="58 foot dive boat at anchor"></div>
    <h3 class="card-title">58' Dive Special</h3>
    <p class="card-text">Using the experience gained over the years, the suggestions given to us by dive charter captains the world over, we have designed and built our Harlow Dive Specials. We listened and incorporated features such as "Fiberglass Stringers" for added durability and low maintenance, "Rear Water Level Entry" for ease of diver entry and exits, and "Cored Cabin Construction" for weight reduction and good looks.</p>
    <div class="card-btn" style="top:210px">Read more</div>
  </article>
  <article class="card" style="left:444px;top:641px">
    <div class="card-img bright" role="img" aria-label="53 foot sport fishing boat at the dock"></div>
    <h3 class="card-title">53' Sport Fish</h3>
    <p class="card-text">Using the experience gained over the years, the suggestions given to us by dive charter captains the world over, we have designed and built our Harlow Dive Specials. We listened and incorporated features such as "Fiberglass Stringers" for added durability and low maintenance, "Rear Water Level Entry" for ease of diver entry and exits, and "Cored Cabin Construction" for weight reduction and good looks.</p>
    <div class="card-btn" style="top:210px">Read more</div>
  </article>
  <article class="card" style="left:53px;top:898px">
    <div class="card-img sea" role="img" aria-label="53 foot dive excursion boat at anchor"></div>
    <h3 class="card-title">53' Dive/Excursion</h3>
    <p class="card-text">Using the experience gained over the years, the suggestions given to us by dive charter captains the world over, we have designed and built our Harlow Dive Specials. We listened and incorporated features such as "Fiberglass Stringers" for added durability and low maintenance, "Rear Water Level Entry" for ease of diver entry and exits, and "Cored Cabin Construction" for weight reduction and good looks.</p>
    <div class="card-btn" style="top:210px">Read more</div>
  </article>
  <article class="card" style="left:249px;top:898px">
    <div class="card-img bright" role="img" aria-label="46 foot dive boat at the dock"></div>
    <h3 class="card-title">46' DiveSpecial</h3>
    <p class="card-text">Using the experience gained over the years, the suggestions given to us by dive charter captains the world over, we have designed and built our Harlow Dive Specials. We listened and incorporated features such as " Fiberglass Stringers" for added durability and low maintenance, " Rear Water Level Entry" for ease of diver entry and exits, and " Cored Cabin Construction" for weight reduction and good looks.</p>
    <div class="card-btn" style="top:210px">Read more</div>
  </article>
  <article class="card" style="left:444px;top:898px">
    <div class="card-img deep" role="img" aria-label="Sport fishing boat cruising on open sea"></div>
    <h3 class="card-title">Title</h3>
    <p class="card-text">Lorem ipsum dolor sit amet consectetur adipisicing elit. Consequatur, aperiam?</p>
    <div class="card-btn" style="top:154px">Read more</div>
  </article>

  <section class="gallery"></section>
  <h2 class="section-title abs" style="left:57px;top:1216px">Gallery</h2>
  <div class="field-label">Choose a boat:</div>
  <div class="select">71' Custom Dive</div>
  <p class="gallery-text">The "New" Harlow 71' x 18' model is now available and the custom possibilities are endless. With over 252 square feet in the salon area and over 240 square feet below, there will be plenty of room for all the amenities you desire.</p>
  <div class="video" role="img" aria-label="Video of the 71 foot custom boat cruising at sea">
    <div class="video-bar">
      <span style="position:absolute;left:2px;top:0">▶</span>
      <span style="position:absolute;left:24px;top:1px">0:00 / 0:2</span>
      <span style="position:absolute;right:4px;top:0">⤢ ⋮</span>
      <div style="position:absolute;left:0;bottom:-3px;width:245px;height:1px;background:#d7e3f3"></div>
    </div>
  </div>

  <div class="contact-info">
    <div class="mini-brand">Harlow</div>
    <strong style="font-size:6.5px">Hours Operation</strong><br>
    Monday - Friday : 10.30 am - 8.30 pm<br>
    Saturday : 10.30 am - 7.00 pm<br>
    Sunday/Public Holidays: Closed<br><br>
    ✆ (555) 201-4470<br>
    ☎ (555) 201-4471<br>
    ✉ Office@harlowboats.com<br>
    Harlow Boats, Inc.<br>
    1200 Harbor Rd.<br>
    Marlow, LA 70000 <span style="color:var(--ink)">USA</span>
  </div>
  <div class="divider"></div>
  <h2 class="section-title abs" style="left:433px;top:1437px">Contact <em>Us</em></h2>
  <div class="form-label" style="top:1477px">First Name</div>
  <div class="input" style="top:1466px">Your name..</div>
  <div class="form-label" style="top:1509px">Last Name</div>
  <div class="input" style="top:1498px">Your last name..</div>
  <div class="form-label" style="top:1540px">Country</div>
  <div class="input" style="top:1529px;color:var(--ink)">Australia<span style="position:absolute;right:5px;top:3px">⌄</span></div>
  <div class="form-label" style="top:1614px">Subject</div>
  <div class="input" style="top:1562px;height:96px">Write something..</div>
  <div class="submit">Submit</div>

  <svg class="footer-wave" viewBox="0 0 670 255" preserveAspectRatio="none" aria-hidden="true">
    <defs>
      <linearGradient id="footGrad" x1="0" y1="0" x2="1" y2="1">
        <stop offset="0" stop-color="#1f4ea8"/>
        <stop offset="1" stop-color="#0f3f96"/>
      </linearGradient>
    </defs>
    <path d="M0 70 C120 30 260 50 380 55 C500 60 600 20 670 0 L670 255 L0 255 Z" fill="#1a56b2"/>
    <path d="M0 78 C130 38 260 58 380 63 C500 68 600 28 670 8 L670 255 L0 255 Z" fill="#ffffff"/>
    <path d="M0 82 C130 42 260 62 380 67 C500 72 600 32 670 12 L670 255 L0 255 Z" fill="url(#footGrad)"/>
  </svg>
  <div class="footer-brand">Harlow<br>Custom Boats</div>
  <div class="foot-col" style="left:201px">
    <h4>Address</h4>
    ✆ (555) 201-4470<br>☎ (555) 201-4471<br>✉ Office@harlowboats.com<br>Harlow Boats, Inc.<br>1200 Harbor Rd.<br>Marlow, LA 70000 <b>USA</b><br>PO BOX 220: Kestrel SA , <b>USA</b>
  </div>
  <div class="foot-col" style="left:374px">
    <h4>Menu</h4>
    About Us<br>Services<br>Contact Us<br>FAQS<br>Request Appointment
  </div>
  <div class="foot-col" style="left:488px">
    <h4>Social Media</h4>
    <div class="social"><i></i><i></i><i></i><i></i></div>
  </div>

</div>
</body>
</html>
```